Business card design needed for Automotive Reconditioning business

I have a logo design i just cant decide on the best color or layout for the business card, I will upload all the files so you can see all colors schemes we are considering. I have other file formats if needed let me know.

Target Market(s)

automotive dealerships

Contact Information for Business Card

HERE are the Descriptions and info needed on the card:
Interior Repair: Leather carpet burns panels dash Deoderize
Dealer products and Vin Verify
( spot for name and cell number) My name is Norman Bexley phone 614 352-4180 Title COO www.QuorvalMotive.com

Font styles to use
Sans Serif
Other font styles liked:
• what ever you think looks best

Requirements
Must have
• Must be able to change the name and phone for employees

```html
<!DOCTYPE html>
<html lang="en">
<head>
<meta charset="utf-8">
<title>Quorval Motive – Business Card</title>
<link rel="stylesheet" href="https://fonts.googleapis.com/css2?family=Open+Sans:wght@300;400;700&family=Cinzel:wght@400&display=swap">
<style>
  :root {
    --page-bg: #2a2a2a;
    --card-black: #0b0b0b;
    --card-charcoal: #1c1c1c;
    --text-white: #f2f2f2;
    --text-soft: #cfcfcf;
    --accent-green: #8cc63f;
    --art-warm-dark: #3a1c0c;
    --art-warm: #6b3414;
    --photo-tone: #2e2e2e;
  }
  * { margin: 0; padding: 0; box-sizing: border-box; }
  html, body {
    width: 1200px;
    height: 716px;
    overflow: hidden;
    background: var(--page-bg);
    font-family: "Open Sans", sans-serif;
  }
  .canvas {
    position: relative;
    width: 1200px;
    height: 716px;
    display: flex;
    align-items: center;
    justify-content: center;
    gap: 48px;
  }
  .card {
    position: relative;
    width: 520px;
    height: 298px;
    border-radius: 4px;
    overflow: hidden;
    box-shadow: 0 14px 30px rgba(0,0,0,0.5);
  }

  /* Services side */
  .card--services {
    background: radial-gradient(ellipse at 40% 30%, #1a1a1a 0%, var(--card-black) 70%);
  }
  .services-list {
    position: absolute;
    top: 30px;
    left: 34px;
    right: 40px;
    color: var(--text-white);
    font-weight: 300;
    font-size: 14px;
    line-height: 1.55;
  }
  .wheel-art {
    position: absolute;
    right: 60px;
    bottom: 26px;
    width: 120px;
    height: 110px;
    background: linear-gradient(160deg, var(--art-warm) 0%, var(--art-warm-dark) 100%);
  }

  /* Identity side */
  .card--identity {
    background: linear-gradient(160deg, #262626 0%, var(--card-charcoal) 45%, #0c0c0c 100%);
  }
  .car-photo {
    position: absolute;
    inset: 0;
    background: linear-gradient(160deg, var(--photo-tone) 0%, #141414 100%);
  }
  .identity {
    position: absolute;
    left: 0;
    right: 0;
    top: 92px;
    text-align: center;
    color: var(--text-white);
  }
  .company-name {
    display: inline-flex;
    align-items: center;
    gap: 10px;
    font-weight: 700;
    font-size: 34px;
    letter-spacing: 1px;
    text-transform: uppercase;
    color: var(--text-white);
  }
  .company-name .mark {
    width: 14px;
    height: 14px;
    background: var(--accent-green);
  }
  .person-name {
    margin-top: 18px;
    font-family: "Cinzel", serif;
    font-size: 18px;
    letter-spacing: 2px;
    text-transform: uppercase;
  }
  .person-title {
    margin-top: 2px;
    font-family: "Cinzel", serif;
    font-size: 13px;
    color: var(--text-soft);
  }
  .person-phone {
    margin-top: 14px;
    font-size: 17px;
    letter-spacing: 0.5px;
  }
</style>
</head>
<body>
  <main class="canvas">
    <section class="card card--services">
      <p class="services-list">
        Interior Repair: Leather carpet burns panels dash Deoderize<br>
        Dealer products and Vin Verify
      </p>
      <div class="wheel-art" role="img" aria-label="Illustration of a car wheel rim wrapped in flames"></div>
    </section>

    <section class="card card--identity">
      <div class="car-photo" role="img" aria-label="Dark photograph of a black sports car"></div>
      <div class="identity">
        <div class="company-name"><span class="mark"></span>Quorval Motive</div>
        <p class="person-name">Norman Bexley</p>
        <p class="person-title">COO</p>
        <p class="person-phone">614 352-4180</p>
      </div>
    </section>
  </main>
</body>
</html>
```